Financial Advisor Resource Firm needs business card design

Need business card design for company in Omaha NE called Tallowbrook Alliance. We provide resources to financial advisors....workshop programs, retirement analysis, and insurance planning. I would like to see designs that use grays, greens, black, and white colors. The final design should communicate 'collaboration' and be simple yet attractive to financial planning clients. I will attached our logo and another picture of a puzzle piece coming together. I would like the incorporate the puzzle picture somehow, maybe on the back somehow, with color or just the gray scale....OR, the picture be the front of the card with 'Tallowbrook' definition on it (see upload) and then company logo, employee name, title, address on the back (see ppt uploaded). The following disclosure needs to be included somewhere- Advisory services offered through Hemstead Ledger, LLC.
Updates

I uploaded a svg and ai file of the logo

Target Market(s)

Financial planning clients and financial advisors....so pretty diverse age range of about 40-70.

Industry/Entity Type

Financial Planning

Contact Information for Business Card

Morris P. Quillfen, MBA
Founder/President
5327 E. Larkspur Avenue
Suite 418
Omaha, NE 68907
Phone- (402) 555-0147
Cell- (402) 555-0193
Fax- (402) 555-0126
email- morris@tallowbrookplan.example
web address- www.tallowbrookplan.example

Colors
1b1b1b
474747
d3d3d3
ffffff
9bcb3c
abd036

Requirements
Must have
• Must include logo provided, must be 2 sided, and must have disclosure...all of these items listed in project description

```html
<!DOCTYPE html>
<html lang="en">
<head>
<meta charset="utf-8">
<title>Tallowbrook Alliance – Business Card</title>
<link href="https://fonts.googleapis.com/css2?family=Source+Sans+3:wght@400;600;700&family=Montserrat:wght@400;600&display=swap" rel="stylesheet">
<style>
  :root {
    --ink: #1b1b1b;
    --graphite: #474747;
    --mist: #d3d3d3;
    --paper: #ffffff;
    --leaf: #9bcb3c;
    --leaf-bright: #abd036;
    --stage-light: #e9eaeb;
    --stage-dark: #cfd0d2;
  }
  html, body {
    margin: 0;
    padding: 0;
    width: 800px;
    height: 1200px;
    overflow: hidden;
  }
  body {
    position: relative;
    background: radial-gradient(ellipse at 50% 50%, var(--stage-light) 0%, var(--stage-dark) 100%);
    font-family: "Source Sans 3", "Helvetica Neue", Arial, sans-serif;
  }
  .card {
    position: absolute;
    left: 148px;
    width: 504px;
    height: 288px;
    overflow: hidden;
  }
  .card--front { top: 174px; background: var(--paper); }
  .card--back { top: 703px; }

  /* front */
  .rule {
    position: absolute;
    left: 0;
    width: 100%;
    height: 2px;
    background: var(--ink);
  }
  .rule--top { top: 17px; }
  .rule--bottom { top: 99px; }
  .name-band {
    position: absolute;
    top: 21px;
    left: 0;
    width: 100%;
    height: 76px;
    background: var(--leaf);
    color: var(--paper);
    text-align: center;
  }
  .name-band__name {
    margin: 0;
    padding-top: 19px;
    font-size: 23px;
    font-weight: 700;
    line-height: 1;
    letter-spacing: 0.1px;
  }
  .name-band__title {
    margin: 6px 0 0;
    font-size: 12.8px;
    font-weight: 400;
    line-height: 1;
  }
  .brand {
    position: absolute;
    left: 20px;
    top: 184px;
    display: flex;
    align-items: center;
    gap: 7px;
  }
  .brand__dot {
    width: 12px;
    height: 12px;
    border-radius: 50%;
    background: var(--leaf);
  }
  .brand__name {
    font-family: "Montserrat", Arial, sans-serif;
    font-weight: 600;
    font-size: 17px;
    color: var(--ink);
    letter-spacing: 0.2px;
  }
  .divider {
    position: absolute;
    left: 242px;
    top: 176px;
    width: 1px;
    height: 44px;
    background: var(--mist);
  }
  .contact {
    position: absolute;
    left: 254px;
    top: 145px;
    color: var(--graphite);
    font-size: 13px;
    line-height: 17px;
  }
  .contact__address { margin: 0 0 3px; }
  .contact__list { list-style: none; margin: 0; padding: 0; }
  .contact__item {
    display: flex;
    align-items: center;
    gap: 5px;
    height: 17px;
  }
  .contact__icon { width: 9px; height: 9px; flex: none; }

  /* back */
  .back-photo {
    position: absolute;
    inset: 0;
    background: radial-gradient(ellipse at 65% 40%, #3a3a3a 0%, #2a2a2a 45%, var(--ink) 100%);
  }
  .back-brand {
    position: absolute;
    left: 0;
    width: 100%;
    top: 112px;
    display: flex;
    justify-content: center;
    align-items: center;
    gap: 10px;
  }
  .back-brand__dot {
    width: 16px;
    height: 16px;
    border-radius: 50%;
    background: var(--paper);
  }
  .back-brand__name {
    font-family: "Montserrat", Arial, sans-serif;
    font-weight: 600;
    font-size: 30px;
    color: var(--paper);
    letter-spacing: 0.5px;
  }
  .tagline {
    position: absolute;
    left: 0;
    width: 100%;
    top: 196px;
    margin: 0;
    text-align: center;
    font-family: "Montserrat", Arial, sans-serif;
    font-size: 12.4px;
    color: var(--paper);
    letter-spacing: 0.1px;
  }
  .disclosure {
    position: absolute;
    left: 0;
    width: 100%;
    bottom: 14px;
    margin: 0;
    text-align: center;
    font-family: "Montserrat", Arial, sans-serif;
    font-size: 8px;
    color: var(--mist);
    letter-spacing: 0.2px;
  }
</style>
</head>
<body>

<section class="card card--front">
  <div class="rule rule--top"></div>
  <header class="name-band">
    <h1 class="name-band__name">Morris P. Quillfen, MBA</h1>
    <p class="name-band__title">Founder/President</p>
  </header>
  <div class="rule rule--bottom"></div>

  <div class="brand">
    <span class="brand__dot"></span>
    <span class="brand__name">Tallowbrook Alliance</span>
  </div>

  <div class="divider"></div>

  <div class="contact">
    <p class="contact__address">5327 E. Larkspur Avenue Suite 418<br>Omaha, NE 68907</p>
    <ul class="contact__list">
      <li class="contact__item">
        <svg class="contact__icon" viewBox="0 0 10 10"><path d="M2 1 L4 1 L4.6 3 L3.4 3.8 Q4.2 5.8 6.2 6.6 L7 5.4 L9 6 L9 8 Q8.5 9 7.5 9 Q1 8 1 2.5 Q1 1.5 2 1Z" fill="#9bcb3c"/></svg>
        (402) 555-0147
      </li>
      <li class="contact__item">
        <svg class="contact__icon" viewBox="0 0 10 10"><rect x="2.5" y="0.5" width="5" height="9" rx="0.8" fill="none" stroke="#9bcb3c" stroke-width="1"/><circle cx="5" cy="8" r="0.6" fill="#9bcb3c"/></svg>
        (402) 555-0193
      </li>
      <li class="contact__item">
        <svg class="contact__icon" viewBox="0 0 10 10"><rect x="2.5" y="0.5" width="5" height="3" fill="#9bcb3c"/><rect x="0.5" y="4" width="9" height="4" rx="0.6" fill="#9bcb3c"/><rect x="2.5" y="7" width="5" height="2.5" fill="#9bcb3c"/></svg>
        (402) 555-0126
      </li>
      <li class="contact__item">
        <svg class="contact__icon" viewBox="0 0 10 10"><rect x="0.5" y="2" width="9" height="6" fill="#9bcb3c"/><path d="M0.5 2 L5 5.5 L9.5 2" fill="none" stroke="#fff" stroke-width="0.9"/></svg>
        morris@tallowbrookplan.example
      </li>
      <li class="contact__item">
        <svg class="contact__icon" viewBox="0 0 10 10"><circle cx="5" cy="5" r="4.3" fill="none" stroke="#9bcb3c" stroke-width="1"/><ellipse cx="5" cy="5" rx="1.8" ry="4.3" fill="none" stroke="#9bcb3c" stroke-width="0.8"/><path d="M0.7 5 H9.3" stroke="#9bcb3c" stroke-width="0.8"/></svg>
        www.tallowbrookplan.example
      </li>
    </ul>
  </div>
</section>

<section class="card card--back">
  <div class="back-photo" role="img" aria-label="Darkened grayscale photograph of hands fitting puzzle pieces together on a table"></div>
  <div class="back-brand">
    <span class="back-brand__dot"></span>
    <span class="back-brand__name">Tallowbrook Alliance</span>
  </div>
  <p class="tagline">TO COME TOGETHER AND UNITE IN COMMON INTEREST AND FOCUS</p>
  <p class="disclosure">Advisory services offered through Hemstead Ledger, LLC</p>
</section>

</body>
</html>
```